Natural and organic skincare brand needs label design!

I need labels designed for my natural and organic skincare brand lumavale. The front of the bottles must contain the logo (image attached) and the following words: Formulated by a Naturopath; Anti-aging therapy; Organic Facial Oil; with CoEnzyme Q10 and Rosehip Seed Oil; 100ml e3.38fl.oz. Colours I would like used include black/white/grey/silver and aqua. I also like the grey woodgrain used on my draft website (check out www.lumavale-skin.com.au). The logo should be silver foil (shiny).The final design should be simple and communicate nature and sophistication. Some designs I like are found in the attachments. I intend to use black or white bottles.

Target Market(s)

women aged 30-50 interested in natural products

Industry/Entity Type

Skin Care Product

Font styles to use
Serif
Sans Serif
Decorative
Script
Other font styles liked:
• Any

Requirements
Must have
• Dimensions: 62mm (w) x 75mm (H) (front label only)
• Must contain the logo (image attached). The logo should be silver foil (shiny). and the following words are to be included on the label:
• Formulated by a Naturopath;
• Anti-aging Therapy;
• Organic Facial Oil;
• with CoEnzyme Q10 and Rosehip Seed Oil;
• 100ml e3.38fl.oz.
Nice to have
• Colours I would like used include black/white/grey/silver and aqua (turquoise). But I am also open to suggestion. I also like the grey woodgrain used on my draft website (check out www.lumavale-skin.com.au)

```html
<!DOCTYPE html>
<html lang="en">
<head>
<meta charset="utf-8">
<title>lumavale – Anti-Aging Therapy front label</title>
<link rel="stylesheet" href="https://fonts.googleapis.com/css2?family=Cinzel:wght@600&family=Dancing+Script:wght@700&family=Lato:ital,wght@0,300;0,400;1,300&display=swap">
<style>
  :root {
    --page: #f3f3f3;
    --label-black: #000000;
    --silver-light: #ffffff;
    --silver-mid: #d9dadc;
    --silver-dark: #9a9ca0;
    --aqua: #5fc3c9;
    --lavender: #b7b3dc;
    --slate: #6f8fa8;
    --ink-dark: #1a1a1a;
    --text-light: #e6e6e6;
    --text-soft: #b9b9b9;
  }
  html, body {
    margin: 0;
    width: 1200px;
    height: 1200px;
    overflow: hidden;
    background: var(--page);
  }
  .canvas {
    position: relative;
    width: 1200px;
    height: 1200px;
  }
  .front-label {
    position: absolute;
    left: 290px;
    top: 225px;
    width: 620px;
    height: 751px;
  }
  .tagline { font-family: "Dancing Script", cursive; font-weight: 700; font-size: 25px; fill: var(--ink-dark); }
  .brand-name { font-family: "Lato", sans-serif; font-weight: 300; font-size: 46px; letter-spacing: 4px; fill: var(--ink-dark); }
  .product-title { font-family: "Cinzel", serif; font-weight: 600; font-size: 28px; letter-spacing: 1px; fill: var(--text-light); }
  .product-detail { font-family: "Lato", sans-serif; font-weight: 300; font-size: 20px; fill: var(--text-light); }
  .volume { font-family: "Lato", sans-serif; font-style: italic; font-weight: 300; font-size: 16px; fill: var(--text-soft); }
</style>
</head>
<body>
<main class="canvas">
  <svg class="front-label" viewBox="0 0 620 751" xmlns="http://www.w3.org/2000/svg">
    <defs>
      <clipPath id="label-shape">
        <rect width="620" height="751" rx="14"/>
      </clipPath>
      <linearGradient id="watercolour-tones" x1="0" y1="0" x2="1" y2="1">
        <stop offset="0" stop-color="var(--aqua)"/>
        <stop offset="0.35" stop-color="var(--lavender)"/>
        <stop offset="0.65" stop-color="var(--slate)"/>
        <stop offset="1" stop-color="var(--aqua)"/>
      </linearGradient>
      <linearGradient id="silver-foil" x1="0" y1="0" x2="1" y2="1">
        <stop offset="0" stop-color="var(--silver-light)"/>
        <stop offset="0.45" stop-color="var(--silver-mid)"/>
        <stop offset="0.7" stop-color="var(--silver-light)"/>
        <stop offset="1" stop-color="var(--silver-dark)"/>
      </linearGradient>
      <path id="tagline-arc" d="M170 75 Q310 0 450 75"/>
    </defs>

    <g clip-path="url(#label-shape)">
      <rect class="label-body" width="620" height="751" fill="var(--label-black)"/>
      <rect class="watercolour-band" width="620" height="244" fill="url(#watercolour-tones)"
            role="img" aria-label="Abstract aqua and lavender watercolour brushstrokes"/>
    </g>

    <text class="tagline"><textPath href="#tagline-arc" startOffset="50%" text-anchor="middle">Formulated by a Naturopath</textPath></text>

    <g class="brand-seal">
      <circle cx="310" cy="234" r="153" fill="url(#silver-foil)" stroke="var(--silver-dark)" stroke-width="2"/>
      <text class="brand-name" x="310" y="250" text-anchor="middle">lumavale</text>
    </g>

    <text class="product-title" x="310" y="461" text-anchor="middle">ANTI-AGING THERAPY</text>
    <text class="product-detail" x="310" y="513" text-anchor="middle">Organic Facial Oil with CoEnzyme Q10</text>
    <text class="product-detail" x="310" y="548" text-anchor="middle">Rosehip Seed Oil</text>
    <text class="volume" x="310" y="720" text-anchor="middle">100ml e3.38fl.oz.</text>
  </svg>
</main>
</body>
</html>
```